Design concept Visual UI of future mobile app - healthcare

Hi,
I'm looking for a top designer, innovative with strong experience in user interface

The app will be connected to a future health website related to depression and addiction by helping the user to track the moods, tired, anxiety using this mobile app.

I attached the deck of the overall project but I can send you a specific presentation for the app only

thanks

Target Market(s)

Switzerland, UK, Germany and France

Industry/Entity Type

Mental Health

Logo Text

Health, hope

Font styles to use
Sans Serif

Colors
cee9f5
33a6d7
0692cd
0255a3
3276b5
85abd2

Requirements
Must have
• keep it simple, easy to navigate
• The user should be able to track the moods on a daily basis,
• sleep time, and rate how the feel on the day
• To be able to get information from the care ledger of vornel
Nice to have
• to be able share this app with a friend

```html
<!DOCTYPE html>
<html lang="en">
<head>
<meta charset="utf-8">
<title>Mindful Day – App Screens</title>
<link href="https://fonts.googleapis.com/css2?family=Roboto:wght@400;500;700&display=swap" rel="stylesheet">
<style>
  :root {
    --page-bg: #f2f2f2;
    --sky-top: #2f8ed4;
    --sky-mid: #3d9ddc;
    --sky-low: #6db6e6;
    --white: #ffffff;
    --tile: rgba(255, 255, 255, 0.22);
    --tile-dark: rgba(2, 85, 163, 0.35);
    --mood-1: #e8400c;
    --mood-2: #ec6a0a;
    --mood-3: #ec8a0f;
    --mood-4: #dcaa32;
    --mood-5: #a89a16;
    --mood-6: #95981a;
    --mood-7: #86901f;
    --mood-8: #7b8626;
    --mood-9: #727a3f;
    --mood-10: #6b6b6b;
    --sleep-box: #2a76c0;
    --photo: #c99a78;
  }
  * { box-sizing: border-box; margin: 0; padding: 0; }
  html, body { width: 1200px; height: 800px; overflow: hidden; }
  body {
    background: var(--page-bg);
    font-family: "Roboto", Arial, sans-serif;
    color: var(--white);
    position: relative;
  }
  .screen {
    position: absolute;
    top: 227px;
    width: 189px;
    height: 335px;
    overflow: hidden;
    background:
      radial-gradient(ellipse 90px 30px at 150px 300px, rgba(255,255,255,0.35), transparent),
      radial-gradient(ellipse 110px 28px at 40px 320px, rgba(255,255,255,0.3), transparent),
      linear-gradient(180deg, var(--sky-top) 0%, var(--sky-mid) 55%, var(--sky-low) 100%);
  }
  .screen--home { left: 233px; }
  .screen--mood { left: 510px; }
  .screen--graphs { left: 786px; }

  .status-bar {
    position: absolute; top: 3px; left: 5px; right: 5px; height: 9px;
    font-size: 5.5px; display: flex; justify-content: space-between; align-items: center;
  }
  .status-bar .time { position: absolute; left: 50%; transform: translateX(-50%); font-weight: 500; }
  .battery { display: inline-block; width: 11px; height: 5px; background: var(--white); border-radius: 1px; margin-left: 2px; vertical-align: middle; }

  .nav-bar {
    position: absolute; top: 25px; left: 0; right: 0; height: 15px;
    display: flex; align-items: center; justify-content: center;
    font-size: 8px; font-weight: 700; letter-spacing: 0.2px;
  }
  .nav-bar .menu { position: absolute; left: 19px; top: 3px; }
  .nav-bar .back { position: absolute; left: 35px; top: 3px; }
  .nav-bar .forward { position: absolute; right: 18px; top: 3px; }

  /* Home */
  .brand-mark {
    position: absolute; top: 60px; left: 78px; width: 34px; height: 34px;
    border-radius: 50%; background: var(--tile-dark); border: 1px solid var(--white);
  }
  .brand-name {
    position: absolute; top: 106px; left: 0; right: 0; text-align: center;
    font-size: 12px; font-weight: 400; letter-spacing: 0.3px;
  }
  .menu-links { position: absolute; top: 140px; left: 35px; width: 119px; list-style: none; }
  .menu-links li {
    height: 17px; margin-bottom: 6px; background: var(--tile);
    font-size: 9.5px; font-weight: 400; text-align: center; line-height: 17px;
  }
  .intro {
    position: absolute; top: 225px; left: 25px; width: 140px;
    font-size: 7.2px; font-weight: 400; line-height: 1.45; text-align: center;
  }
  .messages {
    position: absolute; top: 270px; left: 35px; width: 119px; height: 17px;
    background: var(--tile-dark); font-size: 9.5px; font-weight: 400; line-height: 17px; text-align: center;
  }

  /* Mood */
  .avatar {
    position: absolute; top: 46px; left: 82px; width: 26px; height: 30px;
    background: linear-gradient(180deg, #b88a5a, var(--photo)); border: 1px solid var(--white);
  }
  .question { position: absolute; top: 78px; left: 0; right: 0; text-align: center; font-size: 9.5px; font-weight: 400; }
  .mood-scale { position: absolute; top: 97px; left: 17px; width: 154px; list-style: none; }
  .mood-scale li { height: 17.6px; line-height: 17.6px; text-align: center; font-size: 8px; font-weight: 400; }
  .mood-scale li:nth-child(1) { background: var(--mood-1); }
  .mood-scale li:nth-child(2) { background: var(--mood-2); }
  .mood-scale li:nth-child(3) { background: var(--mood-3); }
  .mood-scale li:nth-child(4) { background: var(--mood-4); }
  .mood-scale li:nth-child(5) { background: var(--mood-5); }
  .mood-scale li:nth-child(6) { background: var(--mood-6); }
  .mood-scale li:nth-child(7) { background: var(--mood-7); }
  .mood-scale li:nth-child(8) { background: var(--mood-8); }
  .mood-scale li:nth-child(9) { background: var(--mood-9); }
  .mood-scale li:nth-child(10) { background: var(--mood-10); }
  .sleep-time { position: absolute; top: 281px; left: 67px; display: flex; align-items: center; gap: 3px; font-size: 8px; font-weight: 700; }
  .sleep-time .label { margin-right: 4px; }
  .sleep-time .digit { background: var(--sleep-box); width: 13px; height: 12px; line-height: 12px; text-align: center; font-weight: 400; font-size: 7.5px; border-radius: 2px; }

  /* Graphs */
  .chart-title { position: absolute; font-size: 5.5px; font-weight: 700; text-align: center; line-height: 1.2; }
  .chart { position: absolute; }
  .axis { position: absolute; font-size: 3px; display: flex; justify-content: space-between; opacity: 0.85; }
  .year-keys { position: absolute; left: 40px; top: 226px; font-size: 3.5px; line-height: 7px; }
</style>
</head>
<body>

<section class="screen screen--home" aria-label="Home screen">
  <div class="status-bar"><span>●●●○○ NOVA</span><span class="time">4:21 PM</span><span>100%<i class="battery"></i></span></div>
  <div class="nav-bar">
    <svg class="menu" width="10" height="8" viewBox="0 0 10 8"><path d="M0 1h10M0 4h10M0 7h10" stroke="#fff" stroke-width="1"/></svg>
    <svg class="forward" width="5" height="8" viewBox="0 0 5 8"><path d="M1 0.5l3 3.5-3 3.5" stroke="#fff" fill="none" stroke-width="0.8"/></svg>
  </div>
  <div class="brand-mark"></div>
  <h1 class="brand-name">MINDFUL DAY</h1>
  <ul class="menu-links">
    <li>Whats New Today?</li>
    <li>Tracking Graphs</li>
    <li>Personal Information</li>
  </ul>
  <p class="intro">According to our studies Mindful Day<br>App has potential to improve<br>your mood by 16%</p>
  <div class="messages">You have 03 messages</div>
</section>

<section class="screen screen--mood" aria-label="Daily mood screen">
  <div class="status-bar"><span>●●●○○ NOVA</span><span class="time">4:21 PM</span><span>100%<i class="battery"></i></span></div>
  <div class="nav-bar">
    <svg class="menu" width="10" height="8" viewBox="0 0 10 8"><path d="M0 1h10M0 4h10M0 7h10" stroke="#fff" stroke-width="1"/></svg>
    <svg class="back" width="5" height="8" viewBox="0 0 5 8"><path d="M4 0.5L1 4l3 3.5" stroke="#fff" fill="none" stroke-width="0.8"/></svg>
    WHATS NEW TODAY
    <svg class="forward" width="5" height="8" viewBox="0 0 5 8"><path d="M1 0.5l3 3.5-3 3.5" stroke="#fff" fill="none" stroke-width="0.8"/></svg>
  </div>
  <div class="avatar" role="img" aria-label="User profile photo"></div>
  <p class="question">How do you feel today ?</p>
  <ul class="mood-scale">
    <li>Insanely Great</li><li>Great</li><li>Very good</li><li>Good</li><li>Okay</li>
    <li>So-so</li><li>Meh</li><li>Bad</li><li>Very bad</li><li>Couldn't be worse</li>
  </ul>
  <div class="sleep-time"><span class="label">Sleep Time</span><span class="digit">08</span><span class="digit">30</span><span class="digit">30</span></div>
</section>

<section class="screen screen--graphs" aria-label="Tracking graphs screen">
  <div class="status-bar"><span>●●●○○ NOVA</span><span class="time">4:21 PM</span><span>100%<i class="battery"></i></span></div>
  <div class="nav-bar">
    <svg class="menu" width="10" height="8" viewBox="0 0 10 8"><path d="M0 1h10M0 4h10M0 7h10" stroke="#fff" stroke-width="1"/></svg>
    <svg class="back" width="5" height="8" viewBox="0 0 5 8"><path d="M4 0.5L1 4l3 3.5" stroke="#fff" fill="none" stroke-width="0.8"/></svg>
    TRACKING GRAPHS
    <svg class="forward" width="5" height="8" viewBox="0 0 5 8"><path d="M1 0.5l3 3.5-3 3.5" stroke="#fff" fill="none" stroke-width="0.8"/></svg>
  </div>

  <svg width="0" height="0" style="position:absolute">
    <defs>
      <linearGradient id="mood-gradient" x1="0" y1="0" x2="0" y2="1">
        <stop offset="0" stop-color="#e83a10"/>
        <stop offset="0.25" stop-color="#f07a18"/>
        <stop offset="0.45" stop-color="#d0a020"/>
        <stop offset="0.65" stop-color="#8c9a26"/>
        <stop offset="0.85" stop-color="#6d7b3c"/>
        <stop offset="1" stop-color="#666666"/>
      </linearGradient>
    </defs>
  </svg>

  <div class="chart-title" style="top:52px;left:8px;width:82px;">WEEK</div>
  <svg class="chart" style="top:65px;left:8px;" width="82" height="101" viewBox="0 0 82 101">
    <rect width="82" height="101" rx="2" fill="url(#mood-gradient)"/>
    <g stroke="rgba(255,255,255,0.25)" stroke-width="0.5">
      <path d="M0 10h82M0 20h82M0 30h82M0 40h82M0 50h82M0 60h82M0 70h82M0 80h82M0 90h82"/>
      <path d="M11.7 0v101M23.4 0v101M35.1 0v101M46.8 0v101M58.5 0v101M70.2 0v101"/>
    </g>
    <rect y="30" width="82" height="10" fill="rgba(255,255,255,0.35)"/>
    <g fill="#fff">
      <circle cx="6" cy="35" r="0.9"/><circle cx="15" cy="25" r="0.9"/><circle cx="25" cy="25" r="0.9"/>
      <circle cx="36" cy="15" r="0.9"/><circle cx="46" cy="35" r="0.9"/><circle cx="56" cy="45" r="0.9"/>
      <circle cx="66" cy="65" r="0.9"/><circle cx="77" cy="35" r="0.9"/>
    </g>
  </svg>
  <div class="axis" style="top:168px;left:8px;width:82px;"><span>Mon</span><span>Tue</span><span>Wed</span><span>Thu</span><span>Fri</span><span>Sat</span><span>Sun</span></div>

  <div class="chart-title" style="top:49px;left:94px;width:87px;">MONTH<br>2015</div>
  <svg class="chart" style="top:65px;left:94px;" width="87" height="101" viewBox="0 0 87 101">
    <rect width="87" height="101" rx="3" fill="url(#mood-gradient)"/>
    <g stroke="rgba(255,255,255,0.15)" stroke-width="0.5"><path d="M12 0v101M24 0v101M36 0v101M48 0v101M60 0v101M72 0v101"/></g>
    <path d="M0 48 C6 40 10 38 16 46 S26 58 32 42 S42 30 48 44 S58 62 64 38 S74 52 80 62 S85 56 87 54" stroke="#fff" stroke-width="0.7" fill="none" opacity="0.8"/>
  </svg>
  <div class="axis" style="top:168px;left:96px;width:83px;"><span>Jan</span><span>Feb</span><span>Mar</span><span>Apr</span><span>May</span><span>Jun</span><span>Jul</span></div>

  <div class="chart-title" style="top:182px;left:53px;width:82px;">YEAR</div>
  <svg class="chart" style="top:191px;left:53px;" width="82" height="100" viewBox="0 0 82 100">
    <rect width="82" height="100" rx="3" fill="url(#mood-gradient)"/>
    <g fill="none" stroke="#fff" stroke-width="0.6" opacity="0.85">
      <path d="M0 48 C6 40 10 55 16 45 S24 30 30 50 S40 62 46 40 S56 35 62 55 S72 60 82 45"/>
      <path d="M0 55 C8 45 12 40 18 52 S28 62 34 44 S44 36 50 58 S60 48 66 40 S76 62 82 52"/>
      <path d="M0 42 C6 58 12 60 20 40 S30 38 36 56 S46 46 54 50 S64 36 70 62 S78 40 82 38"/>
    </g>
  </svg>
  <div class="year-keys"><div>2016</div><div>2015</div><div>2014</div></div>
  <div class="axis" style="top:293px;left:55px;width:78px;"><span>Jan</span><span>Feb</span><span>Mar</span><span>Apr</span><span>May</span><span>Jun</span><span>Jul</span></div>
</section>

</body>
</html>
```